Update Business Card Design

I'm looking to update my business cards. Attached is a photo of the current design. I like the black side so that does not have to be update. The white side needs to be updated. I want the design to be modern and minimalistic.
I am a lawyer and my firm's website is www.brennoxlegalco.com (for reference).
My firm's logo has a horizontal version (which is on the black side of the card) and a vertical version (on the white side). I would prefer to keep the vertical version on the white side and horizontal version on the black side (the logo files are attached).

I am open to redesigning the black side also. I would like one side to have the horizontal logo and the other to have the vertical logo.

```html
<!DOCTYPE html>
<html lang="en">
<head>
<meta charset="utf-8">
<title>Brennox Legal Co. — Business Card</title>
<link href="https://fonts.googleapis.com/css2?family=Open+Sans:wght@400;600;700&display=swap" rel="stylesheet">
<style>
  :root {
    --stage: #333333;
    --card-dark: #0f0f0f;
    --card-light: #ffffff;
    --accent: #12bde3;
    --ink: #555555;
    --rule: #9a9a9a;
  }
  * { box-sizing: border-box; margin: 0; padding: 0; }
  html, body { width: 1200px; height: 780px; overflow: hidden; }
  body {
    background: var(--stage);
    font-family: "Open Sans", Arial, sans-serif;
    display: flex;
    align-items: center;
    justify-content: center;
    gap: 40px;
  }
  .card {
    width: 540px;
    height: 309px;
    border-radius: 24px;
    position: relative;
    overflow: hidden;
  }
  /* Front: horizontal wordmark */
  .card--front {
    background: var(--card-dark);
    display: flex;
    align-items: center;
    justify-content: center;
    gap: 18px;
  }
  .brand-mark {
    width: 46px;
    height: 46px;
    background: var(--accent);
    border-radius: 4px;
  }
  .brand-name {
    color: var(--accent);
    font-weight: 600;
    font-size: 34px;
    letter-spacing: 2px;
    line-height: 1.05;
  }
  /* Back: vertical wordmark + contact */
  .card--back {
    background: var(--card-light);
    display: flex;
    align-items: center;
  }
  .brand-stack {
    width: 230px;
    display: flex;
    flex-direction: column;
    align-items: center;
    gap: 14px;
  }
  .brand-stack .brand-mark { width: 70px; height: 70px; }
  .brand-stack .brand-rule {
    width: 130px;
    height: 2px;
    background: var(--ink);
  }
  .brand-stack .brand-name {
    font-size: 24px;
    letter-spacing: 1.5px;
    text-align: center;
  }
  .divider {
    width: 1px;
    height: 170px;
    background: var(--rule);
  }
  .contact {
    padding-left: 24px;
    color: var(--ink);
    font-size: 12.5px;
    line-height: 1.4;
  }
  .contact__name {
    color: var(--accent);
    font-weight: 700;
    font-size: 19px;
    letter-spacing: .3px;
    line-height: 1.1;
  }
  .contact__title { font-size: 13px; margin-bottom: 10px; }
  .contact__address { margin-bottom: 10px; }
  .contact__list { list-style: none; }
  .contact__list li { display: flex; align-items: center; gap: 6px; }
  .contact__list svg { width: 11px; height: 11px; fill: var(--accent); flex: none; }
</style>
</head>
<body>
  <section class="card card--front" aria-label="Card front">
    <div class="brand-mark"></div>
    <div class="brand-name">BRENNOX<br>LEGAL CO.</div>
  </section>

  <section class="card card--back" aria-label="Card back">
    <div class="brand-stack">
      <div class="brand-mark"></div>
      <div class="brand-rule"></div>
      <div class="brand-name">BRENNOX<br>LEGAL CO.</div>
    </div>
    <div class="divider"></div>
    <div class="contact">
      <p class="contact__name">DANIEL MERCER</p>
      <p class="contact__title">Attorney at Law</p>
      <p class="contact__address">1180 Harlow Avenue, Suite 310<br>Westbrook, CA 90412</p>
      <ul class="contact__list">
        <li><svg viewBox="0 0 12 12"><path d="M1 4c0-2 2-3 5-3s5 1 5 3v1H8V4H4v1H1zM2 6h8l1 5H1z"/></svg>555.204.1187</li>
        <li><svg viewBox="0 0 12 12"><path d="M3 0h6a1 1 0 0 1 1 1v10a1 1 0 0 1-1 1H3a1 1 0 0 1-1-1V1a1 1 0 0 1 1-1zm0 2v8h6V2z"/></svg>555.318.6640</li>
        <li><svg viewBox="0 0 12 12"><path d="M3 0h5v3H3zM1 4h10v5H9v3H3V9H1zm3 5v2h4V9z"/></svg>555.204.1192</li>
        <li><svg viewBox="0 0 12 12"><path d="M0 2h12v8H0zm1 1v.5l5 3 5-3V3z"/></svg>daniel@brennoxlegalco.com</li>
        <li><svg viewBox="0 0 12 12"><circle cx="6" cy="6" r="5.5"/></svg>www.brennoxlegalco.com</li>
      </ul>
    </div>
  </section>
</body>
</html>
```